Innovative mission-driven diversity services company needs launch brochure

Two-sided 8 1/5" x 11" document to demonstrate a new program.

Target Market(s)

Chief Diversity Officers and Hiring Managers at advertising/communications agencies who are looking to attract and hire recently graduated/about to graduate African American students

Industry/Entity Type

It Company

Requirements
Must have
• a very contemporary feel that will well represent the vibrancy, energy, and identity of the African American student population. This is a cause driven organization and that passion and purpose should be conveyed while recognizing that the target audience are corporate executives.

```html
<!DOCTYPE html>
<html lang="en">
<head>
<meta charset="utf-8">
<title>Parallel Path LLC – Launch Brochure</title>
<link rel="stylesheet" href="https://fonts.googleapis.com/css2?family=Roboto:wght@300;400;500;700&family=Roboto+Condensed:wght@700&display=swap">
<style>
:root{
  --bg:#c3c4c6;
  --paper:#ffffff;
  --ink:#3a3a3a;
  --blue:#1b75bb;
  --blue-bright:#1e9ad6;
  --teal:#17a8a0;
  --orange:#f7a823;
  --panel:#f1f1f3;
  --icon:#d2d4d8;
  --icon-soft:#eceef0;
}
*{box-sizing:border-box;margin:0;padding:0}
html,body{width:1200px;height:803px;overflow:hidden;background:var(--bg);font-family:"Roboto",Arial,sans-serif;color:var(--ink)}
.page{position:absolute;top:52px;width:533px;height:690px;background:var(--paper);overflow:hidden}
.page-left{left:43px}
.page-right{left:618px}
.page-foot{position:absolute;left:0;right:0;bottom:0;height:8px;background:linear-gradient(90deg,var(--blue),var(--blue-bright))}
.abs{position:absolute}

/* header */
.hero{position:absolute;left:0;top:0;width:100%;height:143px;background:linear-gradient(100deg,#6b6b6d 0%,#4b4b4d 45%,#5d5d60 70%,#3d3d3f 100%)}
.ribbon{position:absolute;display:flex;align-items:center;justify-content:center;color:#fff;font-weight:300;white-space:nowrap;background:var(--blue-bright);
  clip-path:polygon(0 0,100% 0,95% 50%,100% 100%,0 100%,5% 50%);z-index:2}
.ribbon-title{left:100px;top:24px;width:334px;height:44px;font-size:35px;line-height:44px}
.hero-sub{position:absolute;left:0;top:87px;width:100%;text-align:center;color:#fff;font-size:13.5px;line-height:17px;font-weight:300}
.hero-sub .accent{color:var(--orange);font-weight:400}

/* stat block */
.lead{left:39px;top:169px;width:148px;color:var(--blue);font-size:13px;line-height:14.6px}
.chart{left:186px;top:165px;width:310px;height:127px;background:var(--panel)}
.chart-title{position:absolute;top:10px;width:100%;text-align:center;font-size:10px}
.bar{position:absolute;bottom:36px;width:39px;background:var(--blue);color:#fff;font-size:10px;font-weight:700;text-align:center;padding-top:4px}
.year-band{position:absolute;left:0;right:0;bottom:27px;height:10px;background:var(--teal);color:#fff;font-size:9px;line-height:10px}
.year-band span{position:absolute;width:80px;text-align:center}
.axis-label{position:absolute;bottom:4px;width:70px;text-align:center;font-size:7.5px;line-height:9px;color:#555}
.body-copy{left:39px;top:318px;width:460px;font-size:10.6px;line-height:12.6px}

.teal-bar{position:absolute;left:39px;width:457px;height:25px;background:var(--teal);color:#fff;font-size:11px;line-height:25px;text-align:center;white-space:nowrap}

.article{left:39px;top:406px;width:201px;height:103px;border:1px solid #444;padding:9px 12px}
.article-tag{font-size:5px;font-weight:700;letter-spacing:.5px}
.article-head{font-family:"Roboto Condensed","Arial Narrow",sans-serif;font-size:14px;line-height:16px;margin-top:4px;color:#222}
.share{display:flex;gap:3px;margin-top:4px}
.share i{display:block;width:12px;height:7px;background:#3b6cc4}
.share i:last-child{background:#e44b3b}
.byline{font-size:5px;color:#777;margin-top:6px}
.portrait{left:244px;top:406px;width:97px;height:103px;background:linear-gradient(160deg,#6f5a4f,#2f2724 70%)}
.portrait-cap{position:absolute;left:9px;bottom:4px;color:#eee;font-family:Georgia,serif;font-size:8px;line-height:8px}
.portrait-cap small{font-size:5px}
.quote{left:347px;top:406px;width:149px;height:103px;background:var(--panel);padding:14px 8px;font-size:10.4px;line-height:12.5px}

.issue{position:absolute;top:550px;width:150px;text-align:center;font-size:10.4px;line-height:12.2px}
.issue-img{width:70px;height:70px;border-radius:50%;margin:0 auto 8px}

/* right page */
.mission-head{position:absolute;left:0;top:0;width:100%;height:122px;background:linear-gradient(100deg,#5a5a5c,#3f3f41 60%,#55555a)}
.mission-title{position:absolute;top:19px;width:100%;text-align:center;color:var(--orange);font-size:38px;font-weight:300;white-space:nowrap}
.mission-text{position:absolute;top:61px;left:30px;right:30px;text-align:center;color:#fff;font-size:13.5px;line-height:17px;font-weight:300}
.hub{position:absolute;left:196px;top:264px;width:114px;height:114px;border-radius:50%;background:var(--blue);color:#fff;font-size:25px;font-weight:300;text-align:center;padding-top:60px}
.hub svg{position:absolute;left:38px;top:22px}
.step{position:absolute;text-align:center;font-size:8.3px;line-height:10.3px}
.step b{display:block;color:var(--blue);font-weight:700;font-size:8.6px}
.ribbon-about{left:20px;top:484px;width:292px;height:34px;font-size:23px;justify-content:flex-start;padding-left:18px;
  clip-path:polygon(0 0,100% 0,94% 50%,100% 100%,0 100%)}
.about{position:absolute;left:0;top:509px;width:100%;height:181px;background:linear-gradient(100deg,#5d5d5f,#464648 60%,#58585b);color:#eee;padding:22px 20px 0 24px;font-size:10.6px;line-height:12.6px;font-weight:300}
.about p+p{margin-top:10px}
</style>
</head>
<body>

<section class="page page-left">
  <div class="hero" role="img" aria-label="Soft black and white photo of a young woman"></div>
  <div class="ribbon ribbon-title">Parallel Path LLC</div>
  <p class="hero-sub"><span class="accent">Narrowing the racial diversity gap</span><br>A powerful new approach to increasing the African-American<br>employment rate in the communications industry</p>

  <p class="abs lead">Despite efforts to increase participation, African-American rates of employment in the communications industry have actually declined over the past decade</p>

  <div class="abs chart">
    <div class="chart-title">African-American Proportion of Workforce*</div>
    <div class="bar" style="left:30px;height:62px">11%</div>
    <div class="bar" style="left:110px;height:48px">7%</div>
    <div class="bar" style="left:203px;height:62px">12%</div>
    <div class="bar" style="left:284px;height:44px">5%</div>
    <div class="year-band"><span style="left:50px">2005</span><span style="left:225px">2016</span></div>
    <div class="axis-label" style="left:15px">Overall<br>Workforce</div>
    <div class="axis-label" style="left:95px">Communications<br>Industry</div>
    <div class="axis-label" style="left:190px">Overall<br>Workforce</div>
    <div class="axis-label" style="left:269px">Communications<br>Industry</div>
  </div>

  <p class="abs body-copy">While the communications agency hiring rate of people of Hispanic or Asian origin has reached parity with their overall workforce participation rates, African-American participation has actually dropped by nearly a third. Communications agencies have identified this gap as a critical issue but are falling further behind on AA hiring. &nbsp;*REFERENCE TO COME</p>

  <div class="teal-bar" style="top:378px">CLIENTS HAVE NOW BEGUN TO DIRECTLY EXERT PRESSURE ON THE INDUSTRY</div>

  <div class="abs article">
    <div class="article-tag">BRANDS</div>
    <div class="article-head">Harvest Foods Co Insists That Its Future Agencies Meet Specific Diversity Quotas</div>
    <div class="share"><i></i><i></i><i></i><i></i></div>
    <div class="byline">By Sam Porter | Aug. 31, 2016</div>
  </div>
  <div class="abs portrait" role="img" aria-label="Portrait photo of an agency executive">
    <div class="portrait-cap">Dana Whitfield<br><small>President &amp; CEO</small></div>
  </div>
  <p class="abs quote">“In order to push yourself to have a more diverse work force you have to be intentional about it — and nothing will drive intent faster than a client’s dollar”</p>

  <div class="teal-bar" style="top:523px">CLIENTS HAVE NOW BEGUN TO DIRECTLY EXERT PRESSURE ON THE INDUSTRY</div>

  <div class="issue" style="left:37px">
    <div class="issue-img" role="img" aria-label="Illustration of a face in profile with striped pattern" style="background:linear-gradient(90deg,#f3f0ea 45%,#c9744a 45%,#e4b35e 70%,#9c3e2e)"></div>
    An industry too inwardly focused to realize that it can be offputting</div>
  <div class="issue" style="left:196px">
    <div class="issue-img" role="img" aria-label="Photo of an audience at an industry conference" style="background:radial-gradient(circle at 50% 35%,#b0463f,#4a2a2a 60%,#2a2424)"></div>
    Assuming barriers to hiring all people of color are the same and are not unique to each group</div>
  <div class="issue" style="left:372px">
    <div class="issue-img" role="img" aria-label="Photo of a graduate holding a sign" style="background:radial-gradient(circle at 50% 50%,#e8e8e8 20%,#3b3330 45%,#fff 72%)"></div>
    Dramatic disconnection from the most critical candidate pool that can provide an immediate and lasting impact</div>

  <div class="page-foot"></div>
</section>

<section class="page page-right">
  <div class="mission-head" role="img" aria-label="Dark photo background of students"></div>
  <h1 class="mission-title">The Parallel Path Mission</h1>
  <p class="mission-text">Drive parity in opportunity and representation for the most promising young African-American minds while creating a cultural and competitive advantage for progressive communications organizations</p>

  <svg class="abs" style="left:0;top:0" width="533" height="480" aria-hidden="true">
    <g fill="var(--icon)">
      <path d="M226 138h20a9 9 0 0 1 9 9v5a9 9 0 0 1-9 9h-10l-8 8v-8h-2a9 9 0 0 1-9-9v-5a9 9 0 0 1 9-9z"/>
      <ellipse cx="272" cy="148" rx="20" ry="14"/><path d="M260 158l-5 12 15-9z"/>
      <circle cx="415" cy="214" r="6"/><rect x="405" y="223" width="20" height="9" rx="3"/>
      <rect x="431" y="208" width="22" height="3"/><rect x="431" y="217" width="22" height="3"/><rect x="431" y="226" width="17" height="3"/>
    </g>
    <rect x="398" y="196" width="61" height="46" rx="6" fill="none" stroke="var(--icon)" stroke-width="3"/>
    <g fill="none" stroke="var(--blue)" stroke-width="1.2">
      <path d="M144 233q4-20 24-25"/><path d="M163 204l5 4-5 5"/>
      <path d="M335 208q24 4 27 26"/><path d="M357 230l5 5 4-6"/>
      <path d="M382 348q-2 22-24 26"/><path d="M363 369l-5 5 6 3"/>
      <path d="M257 424q-16 8-35 1"/><path d="M227 420l-5 5 6 3"/>
      <path d="M152 375q-22-4-26-26"/><path d="M121 353l5-5 5 5"/>
    </g>
  </svg>
  <div class="abs" role="img" aria-label="Network person icon" style="left:53px;top:194px;width:56px;height:56px;border-radius:50%;background:var(--icon-soft)"></div>
  <div class="abs" role="img" aria-label="Presenter at whiteboard icon" style="left:436px;top:330px;width:60px;height:58px;border-radius:8px;background:var(--icon-soft)"></div>
  <div class="abs" role="img" aria-label="Support agent with headset icon" style="left:35px;top:353px;width:52px;height:50px;border-radius:50%;background:var(--icon-soft)"></div>

  <div class="hub">Process
    <svg width="40" height="32" viewBox="0 0 40 32" aria-hidden="true" fill="#fff">
      <circle cx="13" cy="14" r="10"/><circle cx="13" cy="14" r="4" fill="var(--blue)"/>
      <circle cx="31" cy="20" r="6"/><circle cx="31" cy="20" r="2.5" fill="var(--blue)"/>
    </svg>
  </div>

  <div class="step" style="left:194px;top:181px;width:118px"><b>Community Connection</b>Parallel Path works closely with the African-American communities within relevant college programs with a strong focus on HBCUs</div>
  <div class="step" style="left:44px;top:263px;width:128px"><b>Community Building</b>Each Parallel Path candidate signs an agreement to initiate a mentoring relationship with a young African American professional hired after them within their organization.</div>
  <div class="step" style="left:329px;top:263px;width:170px"><b>Identification &amp; Vetting</b>Candidates are identified through community connection and formally assessed for relevant agency technology skills, emotional, cultural and academic prowess.</div>
  <div class="step" style="left:94px;top:391px;width:110px"><b>Onboarding Support</b>New hires will be provided innovative e-development platform with personal mentor, to ensure successful onboarding.</div>
  <div class="step" style="left:266px;top:391px;width:222px"><b>Multi-Focal Training</b>Training program specific to advertising industry, to include all major disciplines.<br>Coaching provided to crystallize candidate’s personal brand and voice, to improve the communication of value and reduce time spent ‘trying to figure out.’ Coaching also focuses on personal presentation and professional etiquette training to facilitate corporate integration.</div>

  <div class="ribbon ribbon-about">About Parallel Path LLC</div>
  <div class="about">
    <p>Parallel Path is a B Corp (for-profit social enterprise) created by two principles with direct and complimentary experiences in tackling related challenges.</p>
    <p>Maya Brooks has created a highly successful coaching practice focused on helping soon to graduate, or recently graduated, college students find purpose-driven careers. She is also the founder and Executive Director of the Brightway Foundation which provides guidance and assistance for young adults who are “aging out” of the welfare system with over half of the foundation’s fellows being African-American. Daniel Reyes spent his career in the advertising business culminating in running leading agencies at both Meridian Group and Vantage Holdings. He has personally dealt with the barriers and frustrations in identifying and attracting talent from the African-American business community despite significant corporate efforts. He has also witnessed the significant advantages gained when truly diversified teams are assembled and nurtured.</p>
  </div>
  <div class="page-foot"></div>
</section>

</body>
</html>
```